Letterhead That Inspires Trust

Birchwell Deed Services, LLC, (BDS) fixes technical problems with property deeds. The problems usually surface when someone tries to buy, sell or mortgage a piece of real estate and one of the lawyers involved find a title defect (a lien, an undischarged mortgage, a deceased person still on the title, unpaid taxes, etc.). BDS then gets involved and often has to contact prior property owners to get them to sign paperwork fixing the problem. We need a letterhead that will a) convey the seriousness of what we are trying to do, b) cause the recipients of our letters to recognize the importance of what are trying to do, and c) convey that we are a established and trustworthy company. We want it to include an image that suggests we are a problem solving company. Attached is an image we think might work; you can use it or not. In addition to our name (Birchwell Deed Services, LLC), the letterhead must include our address and phone number: 418 Harlow Avenue, Suite 207, Providence, RI 02915 (401) 555-3726. We are thinking something straightforward without unnecessary colors or graphics.

```html
<!DOCTYPE html>
<html lang="en">
<head>
<meta charset="utf-8">
<title>Birchwell Deed Services, LLC — Stationery</title>
<link rel="stylesheet" href="https://fonts.googleapis.com/css2?family=Open+Sans:wght@400;600&display=swap">
<style>
  :root {
    --brand-green: #42a150;
    --paper: #ffffff;
    --backdrop: #e9e9ea;
    --ink: #4a4a4a;
    --ink-dark: #2e2e2e;
    --signature-tone: #d9d9d9;
  }
  * { box-sizing: border-box; margin: 0; padding: 0; }
  html, body {
    width: 1200px; height: 795px; overflow: hidden;
    background: var(--backdrop);
    font-family: "Open Sans", Arial, sans-serif;
  }
  .stationery { position: relative; width: 1200px; height: 795px; }

  /* Letterhead */
  .letterhead {
    position: absolute; left: 70px; top: 40px;
    width: 506px; height: 715px;
    background: var(--paper);
    box-shadow: 0 2px 10px rgba(0,0,0,0.08);
    padding: 46px 44px 36px 52px;
    color: var(--ink);
    display: flex; flex-direction: column;
  }
  .letterhead-brand {
    align-self: flex-end;
    display: flex; align-items: center; gap: 8px;
    color: var(--brand-green);
    font-size: 15px; font-weight: 600; letter-spacing: 0.02em;
  }
  .brand-square {
    width: 12px; height: 12px; background: var(--brand-green);
  }
  .letter-body { margin-top: 34px; font-size: 9.6px; line-height: 1.6; }
  .salutation { margin-bottom: 14px; }
  .letter-body p.paragraph { margin-bottom: 14px; }
  .closing { margin-top: 4px; }
  .signature-area {
    margin-top: 12px; width: 78px; height: 52px;
    background: var(--signature-tone); border-radius: 4px;
  }
  .letterhead-footer {
    margin-top: auto; text-align: center;
    font-size: 10px; line-height: 1.75; color: var(--ink-dark);
  }
  .contact-row {
    display: flex; justify-content: center; gap: 14px; align-items: center;
  }
  .contact-item { display: inline-flex; align-items: center; gap: 4px; }
  .contact-icon { width: 9px; height: 9px; fill: var(--brand-green); }

  /* Envelope */
  .envelope {
    position: absolute; left: 620px; top: 250px;
    width: 520px; height: 300px;
    background: var(--paper);
    box-shadow: 0 2px 10px rgba(0,0,0,0.08);
    overflow: hidden;
  }
  .envelope-flap {
    position: absolute; left: 0; top: 0; right: 0; height: 130px;
    background: var(--brand-green);
    border-radius: 0 0 12px 12px;
    display: flex; align-items: center; justify-content: center; gap: 8px;
    color: var(--paper);
    font-size: 15px; font-weight: 600; letter-spacing: 0.02em;
  }
  .envelope-flap .brand-square { background: var(--paper); }
</style>
</head>
<body>
<main class="stationery">
  <section class="letterhead">
    <div class="letterhead-brand">
      <span class="brand-square"></span>
      <span class="brand-name">Birchwell Deed Services, LLC</span>
    </div>

    <div class="letter-body">
      <p class="salutation">Dear customer,</p>
      <p class="paragraph">Lorem ipsum dolor sit amet, consectetur adipisicing elit, sed do eiusmod tempor incididunt ut labore et dolore magna aliqua. Ut enim ad minim veniam, quis nostrud exercitation ullamco laboris nisi ut aliquip ex ea commodo consequat. Duis aute irure dolor in reprehenderit in voluptate velit esse cillum dolore eu fugiat nulla pariatur. Excepteur sint occaecat cupidatat non proident, sunt in culpa qui officia deserunt mollit anim id est laborum.</p>
      <p class="paragraph">Lorem ipsum dolor sit amet, consectetur adipisicing elit, sed do eiusmod tempor incididunt ut labore et dolore magna aliqua. Ut enim ad minim veniam, quis nostrud exercitation ullamco laboris nisi ut aliquip ex ea commodo consequat. Duis aute irure dolor in reprehenderit in voluptate velit esse cillum dolore eu fugiat nulla pariatur. Excepteur sint occaecat cupidatat non proident, sunt in culpa qui officia deserunt mollit anim id est laborum.</p>
      <p class="paragraph">Lorem ipsum dolor sit amet, consectetur adipisicing elit, sed do eiusmod tempor incididunt ut labore et dolore magna aliqua. Ut enim ad minim veniam, quis nostrud exercitation ullamco laboris nisi ut aliquip ex ea commodo consequat. Duis aute irure dolor in reprehenderit in voluptate velit esse cillum dolore eu fugiat nulla pariatur. Excepteur sint occaecat cupidatat non proident, sunt in culpa qui officia deserunt mollit anim id est laborum.</p>
      <p class="paragraph">Lorem ipsum dolor sit amet, consectetur adipisicing elit, sed do eiusmod tempor incididunt ut labore et dolore magna aliqua. Ut enim ad minim veniam, quis nostrud exercitation ullamco laboris nisi ut aliquip ex ea commodo consequat. Duis aute irure dolor.</p>
      <p class="closing">Yours Sincerely,</p>
      <div class="signature-area" role="img" aria-label="Handwritten signature"></div>
    </div>

    <footer class="letterhead-footer">
      <div class="footer-name">Birchwell Deed Services, LLC</div>
      <div class="footer-address">418 Harlow Avenue, Suite 207, Providence, RI 02915</div>
      <div class="contact-row">
        <span class="contact-item">
          <svg class="contact-icon" viewBox="0 0 10 10" aria-hidden="true"><path d="M2 0.5 L3.6 2.6 L2.7 3.6 Q3.6 5.6 6.4 7.3 L7.4 6.4 L9.5 8 L8.3 9.5 Q4.5 9.3 1.6 6.2 Q0.3 4.2 0.5 1.8 Z"/></svg>
          (401) 555-3726
        </span>
        <span class="contact-item">
          <svg class="contact-icon" viewBox="0 0 10 10" aria-hidden="true"><path d="M0 2 H10 V8 H0 Z M0.8 2.6 L5 5.6 L9.2 2.6 Z" fill-rule="evenodd"/></svg>
          info@birchwelldeeds.com
        </span>
        <span class="contact-item">
          <svg class="contact-icon" viewBox="0 0 10 10" aria-hidden="true"><circle cx="5" cy="5" r="4.6"/></svg>
          www.birchwelldeeds.com
        </span>
      </div>
    </footer>
  </section>

  <section class="envelope">
    <div class="envelope-flap">
      <span class="brand-square"></span>
      <span class="brand-name">Birchwell Deed Services, LLC</span>
    </div>
  </section>
</main>
</body>
</html>
```